Kelverin Roofing & Restoration Business Card Design

Lookiing for a double sided business card design that will have rounded corners, will look good with Spot UV, Soft Laminate, or Gloss
Front of card should have Logo, Name and Contact Info, License numbers
Back of card should have Logo, maybe other small details

```html
<!DOCTYPE html>
<html lang="en">
<head>
<meta charset="utf-8">
<title>Kelverin Roofing &amp; Restoration – Business Cards</title>
<link href="https://fonts.googleapis.com/css2?family=Montserrat:wght@400;500;700&display=swap" rel="stylesheet">
<style>
  :root{
    --stage:#5e5e5e;
    --card:#1f1f20;
    --card-back:#202021;
    --accent:#1aa7e6;
    --ink:#ffffff;
    --ink-soft:#e6e6e6;
    --spot-uv:#2b2b2c;
  }
  *{box-sizing:border-box;margin:0;padding:0}
  html,body{width:1200px;height:875px;overflow:hidden}
  body{
    background:var(--stage);
    font-family:"Montserrat",Arial,sans-serif;
    display:flex;align-items:center;justify-content:center;gap:48px;
  }
  .card{
    position:relative;width:540px;height:309px;border-radius:22px;overflow:hidden;
  }
  /* back side */
  .card--back{background:var(--card-back);display:flex;align-items:center;justify-content:center}
  .back-brand{display:flex;align-items:center;gap:14px}
  .back-brand__mark{width:30px;height:30px;background:var(--spot-uv)}
  .back-brand__name{
    color:var(--spot-uv);font-weight:700;font-size:30px;line-height:1.15;letter-spacing:1px;text-transform:uppercase;
  }
  /* front side */
  .card--front{background:var(--card)}
  .front-brand{position:absolute;left:40px;top:140px;display:flex;align-items:center;gap:10px}
  .front-brand__mark{width:14px;height:14px;border-radius:50%;background:var(--accent)}
  .front-brand__name{color:var(--ink);font-weight:700;font-size:17px;line-height:1.2;letter-spacing:.5px;text-transform:uppercase}
  .divider{position:absolute;left:276px;top:52px;width:1px;height:168px;background:var(--accent)}
  .contact{position:absolute;left:300px;top:52px;color:var(--ink-soft);font-size:11.5px;line-height:1.45}
  .contact__name{color:var(--accent);font-weight:700;font-size:19px;letter-spacing:.5px;line-height:1.1}
  .contact__role{margin-bottom:12px}
  .contact__address{margin-bottom:12px}
  .contact__row{display:flex;align-items:center;gap:7px}
  .contact__row svg{width:10px;height:10px;flex:none;fill:var(--accent)}
  .accent-band{position:absolute;left:0;right:0;bottom:0;height:9px;background:var(--accent)}
</style>
</head>
<body>
  <section class="card card--back" aria-label="Card back">
    <div class="back-brand">
      <span class="back-brand__mark"></span>
      <span class="back-brand__name">Kelverin<br>Roofing &amp;<br>Restoration</span>
    </div>
  </section>

  <section class="card card--front" aria-label="Card front">
    <div class="front-brand">
      <span class="front-brand__mark"></span>
      <span class="front-brand__name">Kelverin<br>Roofing &amp;<br>Restoration</span>
    </div>
    <div class="divider"></div>
    <div class="contact">
      <p class="contact__name">MARCUS HALE</p>
      <p class="contact__role">Founder &amp; CEO</p>
      <p class="contact__address">840 Linden Ridge Road<br>Fairmont, Ohio 43210</p>
      <p class="contact__row">
        <svg viewBox="0 0 10 10"><path d="M2 0.5 L3.8 2.6 L2.9 3.7 Q4 6 6.3 7.1 L7.4 6.2 L9.5 8 L8.3 9.5 Q1 8 0.5 1.7 Z"/></svg>
        (555) 214-7730
      </p>
      <p class="contact__row">
        <svg viewBox="0 0 10 10"><path d="M0 2 H10 V8 H0 Z M0.6 2.4 L5 5.6 L9.4 2.4 V2.6 L5 6 L0.6 2.6 Z" fill-rule="evenodd"/></svg>
        info@kelverinroofing.com
      </p>
      <p class="contact__row">
        <svg viewBox="0 0 10 10"><circle cx="5" cy="5" r="4.5"/></svg>
        www.kelverinroofing.com
      </p>
    </div>
    <div class="accent-band"></div>
  </section>
</body>
</html>
```